Business Card Design Project

Use our current logo. Clean design.

Industry/Entity Type

Business

Requirements
Must have
• Marisela DUBRANCQ
M. Law
Managing Partner

Alpenvorsa AG
Kornhalmweg 214
CH-3097 Liebefeld

M. +41 79 412 56 27
T. +41 31 928 44 10
F. +41 31 928 44 19

m.dubrancq@alpenvorsa-example.com
www.alpenvorsa-example.com

```html
<!DOCTYPE html>
<html lang="en">
<head>
<meta charset="utf-8">
<title>signal harbor — Business Card</title>
<link rel="stylesheet" href="https://fonts.googleapis.com/css2?family=Cinzel:wght@400;600&family=Montserrat:wght@400;500&display=swap">
<style>
  :root {
    --backdrop: #d9efea;
    --card: #2b2a2c;
    --brand-purple: #a653b8;
    --title-grey: #7c7b7d;
    --contact-text: #dcdcdc;
    --ghost-grey: #4a494b;
  }
  * { margin: 0; padding: 0; box-sizing: border-box; }
  html, body {
    width: 1200px; height: 759px; overflow: hidden;
    background: var(--backdrop);
  }
  .canvas { position: relative; width: 1200px; height: 759px; }

  .card {
    position: absolute;
    width: 500px; height: 300px;
    background: var(--card);
    border-radius: 26px;
    overflow: hidden;
  }
  .card--back { left: 620px; top: 70px; }
  .card--front { left: 80px; top: 380px; }

  /* Front */
  .brand {
    position: absolute; left: 48px; top: 78px;
    display: flex; align-items: center; gap: 14px;
    font-family: "Montserrat", sans-serif; font-weight: 500;
    font-size: 44px; color: var(--brand-purple); letter-spacing: 0.5px;
  }
  .brand__dot {
    width: 18px; height: 18px; border-radius: 50%;
    background: var(--brand-purple);
  }
  .person {
    position: absolute; left: 120px; top: 168px;
    font-family: "Cinzel", serif; font-weight: 600;
    font-size: 19px; line-height: 27px; color: var(--title-grey);
    letter-spacing: 0.6px;
  }

  /* Back */
  .ghost-brand {
    position: absolute; left: 34px; top: 22px;
    font-family: "Montserrat", sans-serif; font-weight: 500;
    font-size: 54px; line-height: 60px; color: var(--ghost-grey);
  }
  .contacts {
    position: absolute; left: 34px; right: 24px; bottom: 40px;
    display: flex; justify-content: space-between;
    font-family: "Montserrat", sans-serif; font-size: 11.5px;
    color: var(--contact-text); letter-spacing: 0.3px;
  }
  .contacts__col { display: flex; flex-direction: column; gap: 14px; }
  .contact-row { display: flex; align-items: center; gap: 12px; line-height: 14px; }
  .contact-row svg { width: 16px; height: 16px; flex: none; fill: var(--brand-purple); }
</style>
</head>
<body>
<main class="canvas">

  <section class="card card--back" aria-label="Business card, back">
    <div class="ghost-brand">signal<br>harbor</div>
    <div class="contacts">
      <div class="contacts__col">
        <div class="contact-row">
          <svg viewBox="0 0 16 16" aria-hidden="true"><path d="M4 1h8v14H4z M5 2.5v10h6v-10z" fill-rule="evenodd"/></svg>
          <span>M. +41 79 412 56 27</span>
        </div>
        <div class="contact-row">
          <svg viewBox="0 0 16 16" aria-hidden="true"><path d="M3 1.5l3 3-1.5 2c1 2 3 4 5 5l2-1.5 3 3-2 2C7 14 2 9 1 3.5z"/></svg>
          <span>T. +41 31 928 44 10</span>
        </div>
        <div class="contact-row">
          <svg viewBox="0 0 16 16" aria-hidden="true"><path d="M4 1h7v4h3v10H2V5h2z M5 2v4h5V2z M4 9h2v2H4z M8 9h2v2H8z M4 12h2v2H4z M8 12h2v2H8z" fill-rule="evenodd"/></svg>
          <span>F. +41 31 928 44 19</span>
        </div>
      </div>
      <div class="contacts__col">
        <div class="contact-row">
          <svg viewBox="0 0 16 16" aria-hidden="true"><path d="M1 3h14v10H1z M2.5 4.5L8 9l5.5-4.5z" fill-rule="evenodd"/></svg>
          <span>m.dubrancq@alpenvorsa-example.com</span>
        </div>
        <div class="contact-row">
          <svg viewBox="0 0 16 16" aria-hidden="true"><path d="M6.5 1a5.5 5.5 0 1 1 0 11 5.5 5.5 0 0 1 0-11zm0 2a3.5 3.5 0 1 0 0 7 3.5 3.5 0 0 0 0-7z M10 10.5l1.5-1.5 4 4-1.5 1.5z" fill-rule="evenodd"/></svg>
          <span>www.alpenvorsa-example.com</span>
        </div>
        <div class="contact-row">
          <svg viewBox="0 0 16 16" aria-hidden="true"><path d="M8 1a5 5 0 0 1 5 5c0 4-5 9-5 9S3 10 3 6a5 5 0 0 1 5-5zm0 3a2 2 0 1 0 0 4 2 2 0 0 0 0-4z" fill-rule="evenodd"/></svg>
          <span>Alpenvorsa AG, Kornhalmweg 214<br>CH-3097 Liebefeld</span>
        </div>
      </div>
    </div>
  </section>

  <section class="card card--front" aria-label="Business card, front">
    <div class="brand"><span>signal harbor</span><span class="brand__dot"></span></div>
    <div class="person">
      <p>Marisela DUBRANCQ</p>
      <p>M. Law</p>
      <p>Managing Partner</p>
    </div>
  </section>

</main>
</body>
</html>
```